Poster for Kirtan Music Event

Design (3) 24" x 36" Posters

I have provided a sample a friend did in Australia: ( Picture No. 4 )

Use all the text on sample poster except the replacement changes below.

Replace with the following text as this is for different location:
Replacement Text:

Every Friday Night 7:00pm-8:30pm
Nohea Breath & Movement Loft
752 Wenmore St Paia

Free Kirtan Experience! or Free Event
Madhava Vani Prabhu & Friends

Optional Text:

A evening of music, singing of spiritual mantras, and refreshments

Bring flowers, musical instruments, friends, or just come with an open heart.

Meditate on transcendental sounds that provide rest for the mind & heart"

An evening of music & singing of sacred mantra's

```html
<!DOCTYPE html>
<html lang="en">
<head>
<meta charset="utf-8">
<title>Kirtan Experience</title>
<link rel="stylesheet" href="https://fonts.googleapis.com/css2?family=Bebas+Neue&family=Dosis:wght@500;600&family=Oswald:wght@300;400&display=swap">
<style>
  :root {
    --bg-deep: #080808;
    --bg-mid: #2a2a2a;
    --peach: #f2b48c;
    --peach-deep: #c9794a;
    --copper: #8a4a2a;
    --cream: #fff3ea;
    --white: #ffffff;
    --smoke: #3b3b3b;
  }
  * { margin: 0; padding: 0; box-sizing: border-box; }
  html, body { width: 800px; height: 1200px; overflow: hidden; background: var(--bg-deep); }
  .poster {
    position: relative;
    width: 800px;
    height: 1200px;
    overflow: hidden;
    background:
      radial-gradient(ellipse 420px 520px at 400px 420px, rgba(201,121,74,0.18), transparent 70%),
      radial-gradient(ellipse 600px 400px at 400px 1000px, rgba(60,60,60,0.5), transparent 70%),
      linear-gradient(180deg, #1b1b1b 0%, var(--bg-deep) 45%, #161616 100%);
    font-family: "Oswald", sans-serif;
    color: var(--white);
  }
  .rule {
    position: absolute;
    left: 24px;
    width: 752px;
    height: 24px;
  }
  .rule--top { top: 38px; }
  .rule--bottom { top: 1144px; }
  .musicians-photo {
    position: absolute;
    left: 36px;
    top: 150px;
    width: 690px;
    height: 420px;
    border-radius: 40px;
    background:
      radial-gradient(ellipse 200px 220px at 260px 200px, rgba(230,220,210,0.55), transparent 70%),
      radial-gradient(ellipse 180px 220px at 560px 220px, rgba(200,190,180,0.45), transparent 70%),
      linear-gradient(180deg, rgba(60,60,60,0.6), rgba(20,20,20,0.2));
    filter: blur(2px);
  }
  .title-band {
    position: absolute;
    left: 0;
    top: 596px;
    width: 800px;
    height: 100px;
    background: linear-gradient(90deg, rgba(0,0,0,0.2), rgba(0,0,0,0.85) 20%, rgba(0,0,0,0.85) 80%, rgba(0,0,0,0.2));
  }
  .seal {
    position: absolute;
    left: 238px;
    top: 544px;
    width: 324px;
    height: 324px;
  }
  .callout {
    position: absolute;
    border-radius: 14px;
    background: linear-gradient(180deg, rgba(201,121,74,0.85), rgba(138,74,42,0.85));
    color: var(--cream);
    font-weight: 300;
    text-align: center;
    line-height: 1.32;
    display: flex;
    align-items: center;
    justify-content: center;
  }
  .callout--invite {
    left: 24px; top: 82px; width: 206px; height: 190px;
    font-size: 21px;
    border-bottom-right-radius: 40px;
  }
  .callout--evening {
    left: 612px; top: 786px; width: 168px; height: 148px;
    font-size: 21px;
    border-top-left-radius: 36px;
    background: linear-gradient(180deg, rgba(70,70,70,0.9), rgba(30,30,30,0.9));
    border: 1px solid rgba(242,180,140,0.35);
  }
  .event-title {
    position: absolute;
    left: 0;
    top: 594px;
    width: 800px;
    text-align: center;
    font-family: "Bebas Neue", sans-serif;
    font-size: 112px;
    line-height: 1;
    letter-spacing: 2px;
    background: linear-gradient(180deg, var(--white) 0%, var(--white) 48%, var(--peach) 52%, var(--peach-deep) 100%);
    -webkit-background-clip: text;
    background-clip: text;
    color: transparent;
    filter: drop-shadow(3px 4px 0 rgba(120,70,40,0.9)) drop-shadow(0 0 10px rgba(0,0,0,0.8));
  }
  .details {
    position: absolute;
    left: 0;
    top: 858px;
    width: 800px;
    text-align: center;
  }
  .details__host {
    font-weight: 300;
    font-size: 17px;
    line-height: 1.55;
  }
  .divider-stars {
    color: var(--white);
    font-size: 12px;
    letter-spacing: 6px;
    line-height: 1;
    margin: 6px 0 8px;
  }
  .details__schedule {
    font-family: "Dosis", sans-serif;
    font-weight: 600;
    font-size: 40px;
    color: var(--peach);
    line-height: 1.1;
    text-shadow: 0 2px 6px rgba(0,0,0,0.8);
  }
  .details__venue {
    font-weight: 300;
    font-size: 23px;
    line-height: 1.42;
  }
</style>
</head>
<body>
<main class="poster">
  <svg class="rule rule--top" viewBox="0 0 752 24" aria-hidden="true">
    <line x1="0" y1="12" x2="290" y2="12" stroke="var(--peach)" stroke-width="2"/>
    <line x1="462" y1="12" x2="752" y2="12" stroke="var(--peach)" stroke-width="2"/>
    <rect x="300" y="6" width="152" height="12" rx="6" fill="var(--peach)" role="img" aria-label="decorative scroll ornament"/>
  </svg>

  <div class="musicians-photo" role="img" aria-label="photo of two kirtan musicians singing, one with guitar and one at a harmonium"></div>

  <div class="callout callout--invite">Join us in the singing<br>of transcendental sounds<br>that provide rest<br>for the mind &amp; heart</div>

  <div class="title-band"></div>

  <svg class="seal" viewBox="0 0 324 324" aria-hidden="true">
    <circle cx="162" cy="162" r="158" fill="none" stroke="var(--smoke)" stroke-width="4"/>
    <circle cx="162" cy="162" r="146" fill="none" stroke="#555" stroke-width="1.5" stroke-dasharray="2 8"/>
    <circle cx="162" cy="162" r="134" fill="none" stroke="var(--smoke)" stroke-width="2"/>
  </svg>

  <h1 class="event-title">Kirtan Experience</h1>

  <div class="callout callout--evening">An evening of<br>music &amp; singing<br>of sacred<br>mantra's</div>

  <section class="details">
    <p class="details__host">Free Event!<br>Madhava Vani Prabhu &amp; Friends</p>
    <p class="divider-stars">★★★</p>
    <p class="details__schedule">Every Friday Night 7:00pm-8:30pm</p>
    <p class="divider-stars">★★★</p>
    <p class="details__venue">Nohea Breath &amp; Movement Loft<br>752 Wenmore St Paia</p>
    <p class="divider-stars">★★★</p>
  </section>

  <svg class="rule rule--bottom" viewBox="0 0 752 24" aria-hidden="true">
    <line x1="0" y1="12" x2="290" y2="12" stroke="var(--peach)" stroke-width="2"/>
    <line x1="462" y1="12" x2="752" y2="12" stroke="var(--peach)" stroke-width="2"/>
    <rect x="300" y="6" width="152" height="12" rx="6" fill="var(--peach)" role="img" aria-label="decorative scroll ornament"/>
  </svg>
</main>
</body>
</html>
```